Job Coaching - Falo; engaging people to improve their work experience

design a website focussed on people
with 4 tabs/pages (+2)
1) landing page
2) Professional
3) Job Coaching
4) Bio
5) Contact
6) references

I've added the text to be used in the documents. The website will be in Dutch, but I've added the translations in green just for you to understand what it is about.

I've added my logo as well, and a flyer I used already. this gives you an idea on how it could look like
Pictures you can find there as well. Other pictures can be added of course
The techical creation of the website is not needed. I need all the designs and information to be able to create it myself.

```html
<!DOCTYPE html>
<html lang="nl">
<head>
<meta charset="utf-8">
<title>Falo Professional Coaching</title>
<link href="https://fonts.googleapis.com/css2?family=Manrope:wght@400;500;600;700&family=Oswald:wght@600;700&family=Playball&display=swap" rel="stylesheet">
<style>
:root{
  --teal:#2fa39a;
  --teal-dark:#1f8a82;
  --ink:#4a4a4a;
  --grey:#6d6d6d;
  --light:#f7f7f7;
  --white:#ffffff;
  --night:#111111;
}
*{margin:0;padding:0;box-sizing:border-box}
html,body{width:1200px;height:2468px;overflow:hidden}
body{font-family:'Manrope',sans-serif;color:var(--ink);background:var(--white);position:relative}
.abs{position:absolute}
.arrow{display:inline-block;vertical-align:middle;margin-left:10px}

/* header */
.site-header{position:absolute;left:0;top:0;width:1200px;height:112px;background:var(--white)}
.brand{left:127px;top:30px;display:flex;align-items:center;gap:12px}
.brand-dot{width:54px;height:54px;border-radius:50%;background:var(--teal)}
.brand-name{font-family:'Manrope',sans-serif;font-weight:700;font-size:46px;color:var(--teal);letter-spacing:1px}
.main-nav a{position:absolute;top:47px;font-size:13px;color:var(--ink);text-decoration:none}
.main-nav a.active{color:var(--teal)}
.call-btn{left:952px;top:38px;width:122px;height:37px;border-radius:19px;background:var(--teal);color:var(--white);font-size:12px;font-weight:700;display:flex;align-items:center;justify-content:center}

/* hero */
.hero{left:0;top:112px;width:1200px;height:563px;background:linear-gradient(180deg,#2a2a2a 0%,#1c1c1c 55%,#262626 100%)}
.hero-greeting{left:126px;top:270px;font-family:'Playball',cursive;font-size:29px;color:#9a9a9a}
.hero-name{left:122px;top:300px;font-family:'Oswald',sans-serif;font-weight:700;font-size:98px;line-height:1.1;color:var(--teal);letter-spacing:1px}
.btn-over{left:125px;top:440px;width:189px;height:47px;border-radius:24px;background:var(--grey);color:var(--white);font-size:20px;font-weight:600;display:flex;align-items:center;justify-content:center}
.hero-portrait{left:710px;top:175px;width:340px;height:400px;border-radius:170px 170px 170px 170px;background:radial-gradient(circle at 40% 30%,#2aa096 0%,#5b5b5b 55%,#8a1f33 100%)}

/* about */
.about{left:0;top:675px;width:1200px;height:543px;background:linear-gradient(90deg,#ffffff 0%,#ffffff 70%,#eeeeee 100%)}
.about-panel{left:0;top:675px;width:380px;height:543px;background:linear-gradient(180deg,#7fd0c6,#39a89d)}
.about-portrait{left:190px;top:728px;width:315px;height:490px;border-radius:120px 120px 0 0;background:linear-gradient(180deg,#8b5a3c 0%,#8c1e30 30%,#7a1a2a 75%,#1e2433 100%)}
.about-title{left:572px;top:752px;font-family:'Oswald',sans-serif;font-weight:700;font-size:43px;line-height:50px;color:#555555}
.about-title span{color:var(--teal)}
.about-text{left:574px;top:872px;width:503px;font-size:12.6px;line-height:17.5px;color:#555555}
.about-text p{margin-bottom:11px}
.btn-aanpak{left:574px;top:1113px;width:173px;height:43px;border-radius:22px;background:var(--teal);color:var(--white);font-size:15px;font-weight:700;display:flex;align-items:center;justify-content:center}

/* cta */
.cta{left:0;top:1218px;width:1200px;height:778px;background:radial-gradient(ellipse at 50% 45%,#3a3a3a 0%,#1f1f1f 50%,#0c0c0c 100%)}
.cta-title{left:0;top:1345px;width:1200px;text-align:center;font-family:'Oswald',sans-serif;font-weight:700;font-size:50px;color:var(--teal)}
.cta-lead{left:0;top:1414px;width:1200px;text-align:center;font-size:15px;line-height:25px;color:var(--white)}
.field{left:341px;width:518px;height:61px;border:1px solid #8a8a8a;border-radius:31px;padding-left:27px;display:flex;align-items:center;font-size:22px;color:#9a9a9a}
.btn-submit{left:466px;top:1796px;width:269px;height:61px;border-radius:31px;background:var(--teal);color:var(--white);font-size:22px;font-weight:700;display:flex;align-items:center;justify-content:center}

/* footer */
.site-footer{left:0;top:1996px;width:1200px;height:472px;background:var(--light)}
.footer-heading{font-size:19px;line-height:23px;font-weight:700;color:var(--teal)}
.partner-icon{left:127px;top:2170px;width:45px;height:46px;border-radius:6px;background:#3f7a3a}
.partner-badge{left:196px;top:2170px;width:163px;height:48px;background:#1d3a8a}
.footer-links{font-size:15px;line-height:25px;color:#555555}
.footer-links .lbl{color:var(--teal)}
.copyright{left:0;top:2424px;width:1200px;text-align:center;font-size:12px;color:#666666}
.footer-rule{left:0;top:2400px;width:1200px;height:1px;background:#eaeaea}
</style>
</head>
<body>

<header class="site-header">
  <div class="abs brand"><span class="brand-dot"></span><span class="brand-name">Falo</span></div>
  <nav class="main-nav">
    <a class="active" style="left:436px">Home</a>
    <a style="left:493px">Professioneel</a>
    <a style="left:596px">Loopbaanbegeleiding</a>
    <a style="left:744px">Bio</a>
    <a style="left:786px">References</a>
    <a style="left:877px">Contact</a>
  </nav>
  <div class="abs call-btn">Bel Me
    <svg class="arrow" width="13" height="13" viewBox="0 0 13 13"><path d="M2 11L11 2M4 2h7v7" stroke="#fff" stroke-width="1.6" fill="none"/></svg>
  </div>
</header>

<section>
  <div class="abs hero" role="img" aria-label="Donkere foto van een zakenman die een trap opklimt tussen hoge gebouwen"></div>
  <div class="abs hero-greeting">Hallo, ik ben loopbaancoach ...</div>
  <h1 class="abs hero-name">JAN VERBEEK</h1>
  <div class="abs btn-over">Over Mij
    <svg class="arrow" width="16" height="16" viewBox="0 0 16 16"><path d="M2 14L14 2M5 2h9v9" stroke="#fff" stroke-width="1.8" fill="none"/></svg>
  </div>
  <div class="abs hero-portrait" role="img" aria-label="Portretfoto van de loopbaancoach in een rood hemd voor een ronde achtergrond"></div>
</section>

<section>
  <div class="abs about" role="img" aria-label="Vervaagde foto van een juichende vrouw op de achtergrond"></div>
  <div class="abs about-panel" role="img" aria-label="Turquoise getinte foto van enthousiaste collega's"></div>
  <div class="abs about-portrait" role="img" aria-label="Foto van de coach staand, in rood hemd"></div>
  <h2 class="abs about-title">“COACHING OP MAAT:<br><span>JOUW SLEUTEL TOT SUCCES”</span></h2>
  <div class="abs about-text">
    <p>Hallo, ik ben Jan Verbeek. Als gepassioneerd loopbaancoach wil ik jou in je kracht zetten bij het uitoefenen van je job, elke dag opnieuw.</p>
    <p>We blijven steeds langer aan de slag en daarom is het vandaag meer dan ooit belangrijk om de nodige aandacht te besteden aan professionele groei en welzijn op het werk.</p>
    <p>Ik ben ervan overtuigd dat mensen vaak tot meer in staat zijn dan ze zelf geloven. Alles begint met het verlangen naar verandering. Wie ben ik? Wat is mijn rol? Wat wil ik écht?</p>
    <p>Als jobcoach ga ik niet voor eenvoudige quick-wins of kant-en-klare tips en tricks. In een geest van openheid, vertrouwen en gelijkwaardigheid gaan we samen op zoek naar de diepere inzichten en duurzame oplossingen die voor jou werken. Coaching is een bewustwordingsproces dat leidt tot het vinden van de antwoorden in jezelf.</p>
  </div>
  <div class="abs btn-aanpak">Mijn Aanpak
    <svg class="arrow" width="13" height="13" viewBox="0 0 13 13"><path d="M2 11L11 2M4 2h7v7" stroke="#fff" stroke-width="1.6" fill="none"/></svg>
  </div>
</section>

<section>
  <div class="abs cta" role="img" aria-label="Donkere foto van een man met aktetas op een pad tussen de wolken"></div>
  <h2 class="abs cta-title">BEGIN VANDAAG!</h2>
  <p class="abs cta-lead">Meld je vandaag nog aan voor een vrijblijvend kennismakingsgesprek<br>en neem de regie van je loopbaan (opnieuw) in handen.</p>
  <div class="abs field" style="top:1505px">Naam</div>
  <div class="abs field" style="top:1596px">E-mail</div>
  <div class="abs field" style="top:1686px;padding-left:36px">Hoe kan ik u helpen?</div>
  <div class="abs btn-submit">Indienen
    <svg class="arrow" width="18" height="18" viewBox="0 0 18 18"><path d="M2 16L16 2M6 2h10v10" stroke="#fff" stroke-width="2" fill="none"/></svg>
  </div>
</section>

<footer>
  <div class="abs site-footer"></div>
  <div class="abs footer-heading" style="left:126px;top:2100px">In samenwerking met het coachingatelier -<br>via de loopbaancheques van Werkpunt</div>
  <div class="abs partner-icon"></div>
  <div class="abs partner-badge"></div>
  <div class="abs footer-heading" style="left:670px;top:2100px">Navigatie</div>
  <div class="abs footer-links" style="left:670px;top:2136px">Home<br>Professioneel<br>Loopbaanbegeleiding<br>Bio<br>Contact<br>References</div>
  <div class="abs footer-heading" style="left:857px;top:2100px">Contact</div>
  <div class="abs footer-links" style="left:857px;top:2136px"><span class="lbl">P -</span> 0470/184629<br><span class="lbl">E -</span> janverbeek@falocoaching.be</div>
  <div class="abs footer-rule"></div>
  <div class="abs copyright">© Copyright 2023 Falo Professional Coaching</div>
</footer>

</body>
</html>
```